Rin3Vox Header

I want a professional Letterhead for my law firm. I'm attaching the letterhead I currently use in Word and PDF form. I'm also attaching my logo, and an example header that I like.

```html
<!DOCTYPE html>
<html lang="en">
<head>
<meta charset="utf-8">
<title>Rin3Vox Letterhead</title>
<link rel="stylesheet" href="https://fonts.googleapis.com/css2?family=Arimo:wght@400&family=Montserrat:wght@400;500;600;800&family=Mrs+Saint+Delafield&display=swap">
<style>
  :root {
    --backdrop: #d9d9d9;
    --paper: #eeeef0;
    --ink: #222326;
    --muted: #7a7a7e;
    --brand-blue: #0d56a6;
    --brand-green: #4b7d3a;
    --rule: #3a3a3c;
  }
  html, body {
    margin: 0;
    width: 1184px;
    height: 1200px;
    overflow: hidden;
    background: var(--backdrop);
  }
  .letterhead {
    position: absolute;
    left: 186px;
    top: 20px;
    width: 811px;
    height: 1160px;
    background: var(--paper);
    font-family: "Montserrat", sans-serif;
    color: var(--muted);
  }
  .brand-name {
    position: absolute;
    left: 53px;
    top: 98px;
    margin: 0;
    font-family: "Montserrat", sans-serif;
    font-weight: 800;
    font-size: 50px;
    line-height: 1;
    letter-spacing: 1px;
    color: var(--ink);
  }
  .header-rule {
    position: absolute;
    left: 53px;
    top: 171px;
    width: 704px;
    height: 1px;
    background: var(--rule);
  }
  .firm-details {
    position: absolute;
    right: 54px;
    top: 39px;
    text-align: right;
    font-family: "Arimo", sans-serif;
    font-size: 13.6px;
    line-height: 17px;
    color: var(--ink);
  }
  .firm-details .firm-title { color: var(--brand-blue); }
  .contact-list {
    list-style: none;
    margin: 4px 0 0;
    padding: 0;
  }
  .contact-list li {
    display: flex;
    justify-content: flex-end;
    align-items: center;
    gap: 5px;
    height: 18px;
  }
  .contact-list svg { width: 12px; height: 12px; fill: var(--brand-blue); }
  .recipient {
    position: absolute;
    left: 82px;
    top: 256px;
  }
  .recipient .label {
    font-size: 14px;
    font-weight: 500;
    letter-spacing: 2px;
    color: var(--ink);
    margin: 0 0 6px;
  }
  .recipient .name {
    font-size: 13.5px;
    font-weight: 600;
    color: var(--brand-blue);
    margin: 0 0 5px;
  }
  .recipient address {
    font-style: normal;
    font-size: 11px;
    line-height: 18.5px;
  }
  .letter-date {
    position: absolute;
    right: 78px;
    top: 256px;
    font-size: 11px;
  }
  .letter-body {
    position: absolute;
    left: 82px;
    top: 413px;
    width: 651px;
    font-size: 11.3px;
    line-height: 14.6px;
    text-align: justify;
  }
  .letter-body p { margin: 0 0 14.6px; }
  .sign-off {
    position: absolute;
    left: 80px;
    top: 814px;
  }
  .signature {
    font-family: "Mrs Saint Delafield", cursive;
    font-size: 34px;
    color: var(--ink);
    line-height: 44px;
  }
  .signer-name {
    margin: 2px 0 0 2px;
    font-size: 12px;
    font-weight: 500;
    color: var(--ink);
  }
  .signer-role { margin: 2px 0 0; font-size: 10px; }
  .footer-band {
    position: absolute;
    left: 0;
    bottom: 2px;
    width: 811px;
    height: 9px;
  }
</style>
</head>
<body>
<main class="letterhead">
  <h1 class="brand-name">RIN3VOX</h1>
  <div class="header-rule"></div>

  <div class="firm-details">
    <div class="firm-title">CASIMIR R. VALDEZ III, ATTORNEY AT LAW, PLLC</div>
    <div>2240 HOLLOWAY AVENUE, SUITE 210</div>
    <div>AUSTIN, TEXAS 78701</div>
    <ul class="contact-list">
      <li>(877) 555-0142 <svg viewBox="0 0 12 12" aria-hidden="true"><path d="M2.5 1 4.5 3.2 3.4 4.6c.7 1.6 2 2.9 3.6 3.6L8.4 7l2.2 2-1 1.6C5.2 10.4 1.4 6.6 1 2.3z"/></svg></li>
      <li>(469) 555-0187 <svg viewBox="0 0 12 12" aria-hidden="true"><path d="M3 1h5l1 1v2H3zM1 5h10v4H9v2H3V9H1zm3 3v2h4V8z"/></svg></li>
      <li>RIN@RIN3VOX.NET <svg viewBox="0 0 12 12" aria-hidden="true"><path d="M1 2.5h10v7H1zm1 1 4 3 4-3z"/></svg></li>
      <li>WWW.RIN3VOX.COM <svg viewBox="0 0 12 12" aria-hidden="true"><circle cx="6" cy="6" r="5"/><path d="M4 3.5c1 .5 1.5 1.5.5 2.5S4 8 5 8.5M8 3c-.5 1 0 2 1 2.5" stroke="#eeeef0" stroke-width="1" fill="none"/></svg></li>
    </ul>
  </div>

  <section class="recipient">
    <p class="label">TO</p>
    <p class="name">Dana Merrow</p>
    <address>Human Resources<br>Northwind Inc.<br>208-B Larkfield Road<br>E89 USA</address>
  </section>
  <time class="letter-date">Friday, 01/01/2018</time>

  <article class="letter-body">
    <p>Lorem ipsum dolor sit amet, consectetuer adipiscing elit, sed diam nonmmy nibh euismod tincidunt ut laoreet dolore magna aliquam erat volutpat. Ut wisi enim ad minim veniam, quis nostrud exerci tationmcorper suscipit lobortis nisl ut aliquip ex ea commodo consequat. Duis autem vel eum iriure dolor in hendrerit in vulputate velit esse molestie consequat, vel illum dolore eu feugiat nulla facilisis at vero eros et accumsan et iusto odio dignissim qui blandit praesent luptatum zzril delenit augue duis dolore te feugait nulla facilisi.</p>
    <p>Nam liber tempor cum soluta nobis eleifend option congue nihil imprdiet doming id quod mazim placerat facer possim assum. Typi non habent claritatem insitam;</p>
    <p>Est usus legentis in iis qui facit eorum claritatem.</p>
    <p>Investigationes demonstraverunt lectores legere me lius quod ii legunt saepius. Claritas est etiam processus dynamicus, qui sequitur mutationem consuetudium lectorum. Mirum est notare quam littera gothica, quam nunc putamus parum claram, anteposuerit litterarum formas humanitatis per seacula quarta decima et quinta decima. Eodem modo typi, qui nunc nobis videntur parum clari, fiant sollemnes in futurum.</p>
    <p>consectetuer adipiscing elit, sed diam nonummy nibh euismod tincidunt ut laoreet dolore magna aliquam erat volutpat. Ut wisi enim ad minim veniam, quis nostrud exerci tation ullamcorper suscipit lobortis nisl ut aliquip ex ea commodo consequat. Duis autem vel eum iriure dolor in hendrerit in vulputate velit esse molestie consequat, vel illum dolore eu feugiat nulla facilisis at vero eros et accumsan et iusto odio dignissim qui blandit praesent luptatum zzril delenit augue duis dolore te feugait nulla facilisi.</p>
    <p>Nam liber tempor cum soluta nobis eleifend option congue nihil imperdiet .</p>
  </article>

  <section class="sign-off">
    <div class="signature">owen hartley</div>
    <p class="signer-name">Owen Hartley</p>
    <p class="signer-role">Managing Director</p>
  </section>

  <svg class="footer-band" viewBox="0 0 811 9" preserveAspectRatio="none" aria-hidden="true">
    <polygon points="0,0 641,0 633,9 0,9" fill="var(--brand-blue)"/>
    <polygon points="649,0 811,0 811,9 641,9" fill="var(--brand-green)"/>
  </svg>
</main>
</body>
</html>
```